Marketing materials for computer support company
trifolds, sign, and magnet
Thank you everyone for your submissions! They were all wonderful.
draft #18 is great - we will spend some time to more carefully review it and give some specific feedback later today. Thanks again
regarding draft #13 and draft #12, these are what we are looking for. The dark photo with the people we would like to go though. We are a small company and don't want to misrepresent that.
We are would use draft #12 for commercial services and draft #13 for residential. Is there anything that could be done to make them slightly different from each other inside though? If not, I'm sure we will find some content to fit - but if someone took one of each brochure, I don't want them to look identical other than the front and color. Maybe even just a different image in the middle of draft #12 where the laptop/wrench image is? Anyway, awesome work!
regarding draft #11, I prefer this to draft #5. Just something doesn't quite fit for me - I'll try to come up with something more specific. Thanks though - this is currently our 2nd favorite
regarding draft #10, I hadn't thought about it before, but I love how one brochure uses mostly blue, and the other uses mostly orange. I also like the flow of both of these. I can't tell if they are tri-fold though. But if you were wondering if we'd like the idea - we do!
-Wade
Also, if it helps, you can checkout what we liked / didn't like in our ongoing stationery / business card content!
Our contest link is: http://www.quintaloft.net/contests/business-card-template-company-stationery
so I will try to be more specific to assist until the unveil it - but bear with me, this is not my area :-) So blue and orange are preferable. Less gradients are better. Curves and circles that flow across the entire front or back for the residential tri-fold connecting the content areas is preferable. Same idea, but with straight angled boxes seems to be what I like on the business tri-fold. Pictures seem more important on the business one (based on existing designs that we have seen), residential can use illustrations in place of pictures. That's what I've got for now!
I just noticed this project is listed as "veiled" even though I did not choose to do so, so I apologize if you can not see the comparisons I am making between each others designs. I will contact support to fix this.
regarding draft #1, thank you for the submission. While I will make some remarks about what I would like to see in the layout, this set of documents is very much along the lines of what I am looking for. The 8.5x11 represents the content of the tri-fold and the magnet has room for a 1" x 3" label. I also like the use of blue! There is something plain about the actual layout though, in comparison to the angles used in draft #4 business tri-fold or curves of draft #4 residential. Thanks again for the submission!
regarding draft #2, I really like the use of our colors and thank you for the submission! I would like more photos as opposed to graphics such as the "help / mouse" or "laptop with stethoscope". I felt the overall feel was very busy and took up a lot of space without providing much room for content. I did like the use of our logo, but I'm ok with it taking up less room in exchange for a really clean look.
regarding draft #3, I like the nerdy magnet guy, but needs room for a 1"x3" thermal label and more room for our name / contact info
regarding draft #4, I like the look of the business tri-fold more than that of the residential. The graphic for the back especially. I think the colors on the residential need to be brighter and more playful. I think the idea of the business tri-fold having more straight lines and sharp angles, while the residential has more curves is great. Just the colors and overall look don't appeal to me. While neither of the magnets would fit a 1x3 label I LOVE how simple the magnet with our logo cutout looks - great idea!

```html
<!DOCTYPE html>
<html lang="en">
<head>
<meta charset="utf-8">
<title>Helpwise Tech – Trifold Set</title>
<link href="https://fonts.googleapis.com/css2?family=Open+Sans:wght@400;600;700;800&display=swap" rel="stylesheet">
<style>
  :root{
    --stage:#5e5043;
    --orange:#f28a1c;
    --orange-deep:#e06b0e;
    --blue:#1d64b8;
    --blue-deep:#123f86;
    --blue-light:#3f8fde;
    --white:#ffffff;
    --ink:#2b2b2b;
    --muted:#6d6d6d;
    --label:#f1ece4;
  }
  *{box-sizing:border-box;margin:0;padding:0}
  html,body{width:1200px;height:895px;overflow:hidden}
  body{background:var(--stage);font-family:"Open Sans",Arial,sans-serif;position:relative}
  .piece-label{position:absolute;color:var(--label);font-size:14px;font-weight:400;letter-spacing:.2px}
  .piece{position:absolute;background:var(--white);overflow:hidden;box-shadow:0 4px 14px rgba(0,0,0,.35)}
  .panel{position:absolute;top:0;bottom:0;overflow:hidden}
  .fold{position:absolute;top:0;bottom:0;width:1px;background:rgba(0,0,0,.08)}
  .abs{position:absolute}
  .photo{position:absolute}
  .deco{position:absolute;z-index:1}
  .brand{display:flex;align-items:center;gap:6px;position:absolute;font-weight:700;white-space:nowrap;z-index:2}
  .brand-mark{display:inline-block;background:var(--orange)}
  .small{font-size:7px;line-height:1.4;z-index:2}
  .url{position:absolute;font-size:8px;font-weight:600;color:var(--white);z-index:2;white-space:nowrap}
  .repairs-title{z-index:2}
  .bullets{list-style:none;z-index:2}
  .bullets li{font-size:8px;color:var(--white);line-height:1.65;padding-left:10px;position:relative}
  .bullets li::before{content:"";position:absolute;left:0;top:5px;width:5px;height:5px;background:var(--white);border-radius:50%}
  .headline{position:absolute;font-weight:700;color:var(--white);line-height:1.05;z-index:2}
  .biz-title{position:absolute;font-weight:800;line-height:1;z-index:2}
  .biz-sub{position:absolute;font-size:7px;font-weight:600;z-index:2}
</style>
</head>
<body>

<!-- Residential trifold – face -->
<div class="piece-label" style="left:40px;top:12px">residential services trifold - face</div>
<div class="piece res-face" style="left:36px;top:36px;width:546px;height:352px">
  <!-- left panel -->
  <div class="panel" style="left:0;width:182px">
    <div class="abs" style="left:0;top:0;width:182px;height:148px;background:var(--orange)"></div>
    <div class="abs repairs-title" style="left:10px;top:16px;font-size:10px;font-weight:700;color:var(--white);letter-spacing:1px">Common repairs:</div>
    <ul class="bullets abs" style="left:12px;top:34px">
      <li>Virus and spyware removal</li>
      <li>Network setup and repair</li>
      <li>Data backup and recovery</li>
      <li>Hardware upgrades</li>
      <li>Slow PC tune ups</li>
      <li>Wireless printer setup</li>
    </ul>
    <div class="photo" role="img" aria-label="Photo of a frustrated man holding a laptop" style="left:0;top:148px;width:90px;height:100px;background:linear-gradient(160deg,#d9d9d9,#7a7a7a)"></div>
    <p class="small abs" style="left:10px;top:262px;width:162px;color:var(--muted)">We fix home computers quickly and explain every step in plain words.</p>
  </div>
  <div class="fold" style="left:182px"></div>
  <!-- middle panel -->
  <div class="panel" style="left:182px;width:182px">
    <div class="abs" style="left:0;top:0;width:182px;height:26px;background:var(--orange)"></div>
    <p class="small abs" style="left:10px;top:36px;width:162px;color:var(--ink)">Friendly local technicians who come to your home and get you working again.</p>
    <div class="photo" role="img" aria-label="Photo of a keyboard with a red help key" style="left:0;top:97px;width:182px;height:123px;background:linear-gradient(135deg,#c9d3cf,#7d8c88 60%,#c0392b 61%,#9e2a20)"></div>
    <div class="abs" style="left:0;top:220px;width:182px;height:132px;background:var(--blue)"></div>
    <div class="brand" style="left:40px;top:240px;font-size:12px;color:var(--white)"><span class="brand-mark" style="width:12px;height:12px"></span>Helpwise Tech</div>
    <p class="small abs" style="left:40px;top:266px;color:var(--white)">Call today to book a visit.</p>
    <div class="url" style="left:45px;top:318px">www.helpwisetech.com</div>
  </div>
  <div class="fold" style="left:364px"></div>
  <!-- right panel -->
  <div class="panel" style="left:364px;width:182px">
    <div class="abs" style="left:0;top:0;width:182px;height:26px;background:var(--orange)"></div>
    <div class="brand" style="left:44px;top:34px;font-size:12px;color:var(--blue)"><span class="brand-mark" style="width:12px;height:12px"></span>Helpwise Tech</div>
    <div class="photo" role="img" aria-label="Photo of a smiling support agent wearing a headset" style="left:0;top:62px;width:182px;height:150px;background:linear-gradient(120deg,#e9e2da,#b49a86 55%,#5a3f30)"></div>
    <div class="abs" style="left:0;top:212px;width:182px;height:140px;background:var(--blue)"></div>
    <div class="headline" style="left:62px;top:262px;font-size:17px">Lorem Ipsum<br>software like</div>
    <div class="abs small" style="left:120px;top:302px;color:var(--white)">lorem ipsum</div>
  </div>
  <!-- flowing curves across the face -->
  <svg class="deco" style="left:0;top:0" width="546" height="352" viewBox="0 0 546 352" aria-hidden="true">
    <path d="M0 12 C140 4 300 20 546 8 L546 0 L0 0Z" fill="var(--orange-deep)"/>
    <path d="M182 220 C300 196 420 236 546 206 L546 224 C420 250 300 212 182 236Z" fill="var(--blue-light)"/>
    <path d="M0 148 C60 140 120 156 182 148" stroke="var(--white)" stroke-width="3" fill="none"/>
    <path d="M0 342 C180 334 360 350 546 338 L546 352 L0 352Z" fill="var(--blue-deep)"/>
  </svg>
</div>

<!-- Residential trifold – presentation -->
<div class="piece-label" style="left:640px;top:12px">residential services trifold - presentation</div>
<div class="piece" style="left:635px;top:97px;width:250px;height:290px">
  <div class="abs" style="left:0;top:0;width:250px;height:22px;background:var(--orange)"></div>
  <div class="brand" style="left:58px;top:30px;font-size:14px;color:var(--blue)"><span class="brand-mark" style="width:13px;height:13px"></span>Helpwise Tech</div>
  <div class="photo" role="img" aria-label="Photo of a smiling support agent wearing a headset" style="left:0;top:60px;width:250px;height:125px;background:linear-gradient(120deg,#e9e2da,#b49a86 55%,#5a3f30)"></div>
  <div class="abs" style="left:0;top:185px;width:250px;height:105px;background:var(--blue)"></div>
  <svg class="deco" style="left:0;top:170px" width="250" height="40" viewBox="0 0 250 40" aria-hidden="true"><path d="M0 30 C80 5 170 35 250 10 L250 20 C170 45 80 15 0 40Z" fill="var(--blue-light)"/></svg>
  <div class="headline" style="left:90px;top:212px;font-size:18px">Lorem Ipsum<br>software like</div>
  <div class="abs small" style="left:166px;top:254px;color:var(--white)">lorem ipsum</div>
  <div class="url" style="left:78px;top:274px">www.helpwisetech.com</div>
</div>

<!-- One sided version -->
<div class="piece-label" style="left:975px;top:158px">one sided version</div>
<div class="piece" style="left:933px;top:182px;width:206px;height:327px">
  <div class="brand" style="left:70px;top:34px;font-size:11px;color:var(--blue)"><span class="brand-mark" style="width:11px;height:11px"></span>Helpwise Tech</div>
  <div class="photo" role="img" aria-label="Photo of a hand working on a computer's internal cables" style="left:0;top:74px;width:206px;height:110px;background:linear-gradient(135deg,#d7dde3,#8e9aa6 60%,#4d5866)"></div>
  <svg class="deco" style="left:0;top:168px" width="206" height="50" viewBox="0 0 206 50" aria-hidden="true"><path d="M0 16 L206 0 L206 26 L0 44Z" fill="var(--blue)"/><path d="M120 10 L206 0 L206 12 L120 22Z" fill="var(--orange)"/></svg>
  <p class="small abs" style="left:110px;top:220px;color:var(--muted)">Home and office support</p>
  <div class="abs" style="left:120px;top:236px;font-size:11px;font-weight:700;color:var(--blue)">(555) 010 2040</div>
  <div class="abs" style="left:120px;top:252px;font-size:7px;color:var(--orange)">www.helpwisetech.com</div>
  <p class="small abs" style="left:12px;top:280px;width:182px;color:var(--muted)">Service plans for every budget with same day visits available.</p>
</div>

<!-- Business trifold – face -->
<div class="piece-label" style="left:40px;top:450px">business services trifold - face</div>
<div class="piece" style="left:36px;top:473px;width:546px;height:388px">
  <!-- left panel -->
  <div class="panel" style="left:0;width:182px">
    <div class="biz-title" style="left:12px;top:18px;font-size:17px;color:var(--blue)">LOREM IPSUM</div>
    <div class="biz-sub" style="left:12px;top:38px;color:var(--orange)">ut wisi enim ad minim veniam</div>
    <p class="small abs" style="left:12px;top:60px;width:158px;color:var(--ink);font-weight:700">Reliable IT support for small offices, from servers to desktops.</p>
    <p class="small abs" style="left:12px;top:86px;width:158px;color:var(--muted)">We keep your systems secure, backed up and running.</p>
    <div class="photo" role="img" aria-label="Photo of a technician plugging cables into network hardware" style="left:0;top:150px;width:182px;height:238px;background:linear-gradient(150deg,#eef0f2,#b9c3ca 50%,#6e8a5c)"></div>
  </div>
  <div class="fold" style="left:182px"></div>
  <!-- middle panel -->
  <div class="panel" style="left:182px;width:182px;background:var(--orange)">
    <div class="photo" role="img" aria-label="Photo of server rack cabling" style="left:0;top:0;width:182px;height:80px;background:linear-gradient(135deg,#3a8a6a,#1f4d46)"></div>
    <svg class="deco" style="left:0;top:60px" width="182" height="60" viewBox="0 0 182 60" aria-hidden="true"><path d="M0 20 L182 0 L182 60 L0 60Z" fill="var(--orange)"/></svg>
    <div class="biz-title" style="left:16px;top:118px;font-size:22px;color:var(--white)">LOREM IPSUM</div>
    <div class="biz-sub" style="left:16px;top:142px;color:var(--white)">ut wisi enim ad minim veniam</div>
    <p class="small abs" style="left:16px;top:166px;width:150px;color:var(--white)">Managed networks, on site visits and remote help desk.</p>
    <div class="brand" style="left:36px;top:276px;font-size:12px;color:var(--white)"><span class="brand-mark" style="width:12px;height:12px;background:var(--white)"></span>Helpwise Tech</div>
    <div class="abs" style="left:0;top:350px;width:182px;height:38px;background:var(--blue)"></div>
    <div class="url" style="left:60px;top:365px">www.domain.com</div>
  </div>
  <div class="fold" style="left:364px"></div>
  <!-- right panel -->
  <div class="panel" style="left:364px;width:182px;background:var(--blue)">
    <div class="photo" role="img" aria-label="Photo of a technician working in a server room" style="left:0;top:0;width:182px;height:170px;background:linear-gradient(120deg,#c8d6e4,#6d87a8 55%,#2b3d5c)"></div>
    <svg class="deco" style="left:0;top:150px" width="182" height="40" viewBox="0 0 182 40" aria-hidden="true"><path d="M0 40 L182 0 L182 40Z" fill="var(--blue)"/></svg>
    <div class="biz-title" style="left:20px;top:186px;font-size:20px;color:var(--white)">LOREM IPSUM</div>
    <div class="biz-sub" style="left:20px;top:208px;color:var(--white)">ut wisi enim ad minim veniam</div>
    <svg class="deco" style="left:104px;top:226px" width="70" height="60" viewBox="0 0 70 60" aria-hidden="true">
      <rect x="0" y="0" width="20" height="20" fill="var(--blue-light)" opacity=".6"/>
      <rect x="24" y="0" width="20" height="20" fill="var(--blue-light)" opacity=".4"/>
      <rect x="48" y="0" width="20" height="20" fill="var(--blue-light)" opacity=".7"/>
      <rect x="24" y="24" width="20" height="20" fill="var(--blue-light)" opacity=".5"/>
      <rect x="48" y="24" width="20" height="20" fill="var(--blue-light)" opacity=".3"/>
    </svg>
    <div class="brand" style="left:36px;top:300px;font-size:12px;color:var(--white)"><span class="brand-mark" style="width:12px;height:12px"></span>Helpwise Tech</div>
    <div class="abs" style="left:0;top:350px;width:182px;height:38px;background:var(--blue-deep)"></div>
    <div class="url" style="left:60px;top:365px">www.domain.com</div>
  </div>
</div>

<!-- Business trifold – presentation -->
<div class="piece-label" style="left:640px;top:462px">business services trifold - presentation</div>
<div class="piece" style="left:635px;top:485px;width:238px;height:363px;background:var(--blue)">
  <div class="photo" role="img" aria-label="Photo of a technician working in a server room" style="left:0;top:0;width:238px;height:180px;background:linear-gradient(120deg,#c8d6e4,#6d87a8 55%,#2b3d5c)"></div>
  <svg class="deco" style="left:0;top:150px" width="238" height="50" viewBox="0 0 238 50" aria-hidden="true"><path d="M0 50 L238 0 L238 50Z" fill="var(--blue)"/></svg>
  <div class="biz-title" style="left:24px;top:196px;font-size:24px;color:var(--white)">LOREM IPSUM</div>
  <div class="biz-sub" style="left:24px;top:222px;color:var(--white)">ut wisi enim ad minim veniam</div>
  <svg class="deco" style="left:150px;top:240px" width="80" height="50" viewBox="0 0 80 50" aria-hidden="true">
    <rect x="0" y="0" width="22" height="22" fill="var(--blue-light)" opacity=".6"/>
    <rect x="26" y="0" width="22" height="22" fill="var(--blue-light)" opacity=".4"/>
    <rect x="52" y="0" width="22" height="22" fill="var(--blue-light)" opacity=".7"/>
    <rect x="26" y="26" width="22" height="22" fill="var(--blue-light)" opacity=".5"/>
  </svg>
  <div class="brand" style="left:56px;top:296px;font-size:14px;color:var(--white)"><span class="brand-mark" style="width:13px;height:13px"></span>Helpwise Tech</div>
  <div class="abs" style="left:0;top:328px;width:238px;height:35px;background:var(--blue-deep)"></div>
  <div class="url" style="left:84px;top:341px">www.domain.com</div>
</div>

</body>
</html>
```